updated documents

Hi i have included a new picture for the about us section, i have also included the updated word document, all changes have been highlighted.

Thanks,

Brett

```html
<!DOCTYPE html>
<html lang="en">
<head>
<meta charset="utf-8">
<title>Crestline Property Services – Brochure Cover</title>
<link rel="stylesheet" href="https://fonts.googleapis.com/css2?family=Source+Sans+3:wght@300;400;500;600&display=swap">
<style>
  :root {
    --ink-black: #050505;
    --photo-shadow: #1f1f1f;
    --photo-dark: #3b3b3b;
    --photo-mid: #707070;
    --photo-light: #b4b4b4;
    --photo-highlight: #d2d2d2;
    --photo-tint: rgba(166, 207, 44, 0.18);
    --panel: rgba(165, 165, 165, 0.86);
    --white: #ffffff;
    --brand-grey: #474747;
    --brand-green: #a6cf2c;
    --fold-line: rgba(255, 255, 255, 0.75);
  }
  * { margin: 0; padding: 0; box-sizing: border-box; }
  html, body { width: 1200px; height: 852px; overflow: hidden; background: var(--ink-black); }
  body { font-family: "Source Sans 3", "Helvetica Neue", Arial, sans-serif; }

  .cover {
    position: relative;
    width: 1200px;
    height: 852px;
    overflow: hidden;
  }
  .city-photo {
    position: absolute;
    left: 0; top: 0;
    width: 1200px; height: 800px;
    background:
      radial-gradient(ellipse 90px 420px at 345px 260px, var(--photo-highlight) 0%, transparent 100%),
      radial-gradient(ellipse 30px 300px at 370px 250px, var(--photo-tint) 0%, transparent 100%),
      radial-gradient(ellipse 160px 140px at 560px 110px, var(--photo-light) 0%, transparent 100%),
      radial-gradient(ellipse 140px 160px at 760px 330px, var(--photo-light) 0%, transparent 100%),
      radial-gradient(ellipse 110px 120px at 190px 230px, var(--photo-light) 0%, transparent 100%),
      radial-gradient(ellipse 220px 200px at 1150px 760px, var(--photo-highlight) 0%, transparent 100%),
      radial-gradient(ellipse 170px 260px at 1000px 260px, var(--photo-shadow) 0%, transparent 100%),
      radial-gradient(ellipse 120px 360px at 530px 420px, var(--photo-shadow) 0%, transparent 100%),
      radial-gradient(ellipse 180px 220px at 60px 420px, var(--photo-shadow) 0%, transparent 100%),
      radial-gradient(ellipse 200px 120px at 870px 40px, var(--photo-dark) 0%, transparent 100%),
      linear-gradient(155deg, var(--photo-mid) 0%, var(--photo-dark) 40%, var(--photo-mid) 70%, var(--photo-light) 100%);
  }
  .footer-band {
    position: absolute;
    left: 0; top: 800px;
    width: 1200px; height: 52px;
    background: var(--ink-black);
  }
  .fold-line {
    position: absolute;
    left: 596px; top: 0;
    width: 1px; height: 852px;
    background: var(--fold-line);
  }
  .panel {
    position: absolute;
    top: 450px;
    width: 424px;
    height: 288px;
    background: var(--panel);
  }
  .panel--contact { left: 86px; }
  .panel--brand { left: 686px; }

  .contact-title {
    position: absolute;
    top: 76px; left: 0; width: 100%;
    text-align: center;
    color: var(--white);
    font-size: 25px;
    font-weight: 500;
    letter-spacing: 0.6px;
  }
  .contact-list {
    position: absolute;
    top: 120px; left: 64px;
    list-style: none;
  }
  .contact-list li {
    display: flex;
    align-items: center;
    height: 24px;
    color: var(--white);
    font-size: 14.5px;
    font-weight: 300;
    letter-spacing: -0.2px;
  }
  .contact-icon {
    width: 13px; height: 13px;
    margin-right: 6px;
    flex: none;
  }

  .brand-name {
    position: absolute;
    top: 176px; left: 0; width: 100%;
    display: flex;
    justify-content: center;
    align-items: center;
    gap: 10px;
    color: var(--brand-grey);
    font-size: 18px;
    font-weight: 400;
    letter-spacing: 1.2px;
    text-transform: uppercase;
  }
  .brand-mark {
    width: 13px; height: 13px;
    background: var(--brand-green);
  }

  .tagline {
    position: absolute;
    top: 814px; left: 596px; width: 604px;
    text-align: center;
    color: var(--white);
    font-size: 19px;
    font-weight: 500;
    letter-spacing: 0.5px;
  }
</style>
</head>
<body>
<main class="cover">
  <div class="city-photo" role="img" aria-label="Black-and-white aerial photograph of a dense city grid with skyscrapers, a construction crane and green-tinted taxis on the avenues"></div>
  <div class="footer-band"></div>
  <div class="fold-line"></div>

  <section class="panel panel--contact">
    <h2 class="contact-title">Contact Us</h2>
    <ul class="contact-list">
      <li>
        <svg class="contact-icon" viewBox="0 0 14 14" aria-hidden="true"><path d="M3 1.5 L5 1.5 L6 4.5 L4.6 5.6 Q5.6 8.4 8.4 9.4 L9.5 8 L12.5 9 L12.5 11 Q12 12.5 10.5 12.5 Q2 11.5 1.5 3.5 Q1.5 1.8 3 1.5 Z" fill="none" stroke="#fff" stroke-width="1"/></svg>
        0400 618 272
      </li>
      <li>
        <svg class="contact-icon" viewBox="0 0 14 14" aria-hidden="true"><rect x="1" y="3" width="12" height="8" fill="none" stroke="#fff" stroke-width="1"/><path d="M1 3 L7 8 L13 3" fill="none" stroke="#fff" stroke-width="1"/></svg>
        brettv@crestlineps.com.au
      </li>
      <li>
        <svg class="contact-icon" viewBox="0 0 14 14" aria-hidden="true"><circle cx="7" cy="7" r="5.5" fill="none" stroke="#fff" stroke-width="1"/><ellipse cx="7" cy="7" rx="2.4" ry="5.5" fill="none" stroke="#fff" stroke-width="0.8"/><line x1="1.5" y1="7" x2="12.5" y2="7" stroke="#fff" stroke-width="0.8"/></svg>
        www.crestlinepropertyservices.com
      </li>
      <li>
        <svg class="contact-icon" viewBox="0 0 14 14" aria-hidden="true"><circle cx="7" cy="7" r="3" fill="#fff"/></svg>
        www.friendbook.com/crestlinepropertyservices
      </li>
    </ul>
  </section>

  <section class="panel panel--brand">
    <div class="brand-name"><span class="brand-mark"></span>Crestline Property Services</div>
  </section>

  <p class="tagline">Your Best Partner in Building Maintenance</p>
</main>
</body>
</html>
```